NEW Escape Room. Fun, Dark and Mysterious.

Escape Room Website. Bookings and scheduling of appointments will be organised with Bookvane through the site. Most appointments will be created online through the booking system with some payments coming through in person by drop-ins. Groups will be from 2 - 8 people with a sliding scale of prices. We will start with one game playable and one saying coming soon. We will also eventually have 4 games up and running at once so will need it to be able to expand. We don't have any images of the rooms because it all relies heavily on mystery. Appointments are each 1 hour long with 30 minutes in between.

Target Market(s)

15-35 year olds

Coding

Coded - Design and coding required

Number of Pages Required

5+ page

Font styles to use
Decorative

Colors

Designer to choose colors to be used in the design.

Requirements
Must have
• Graphics showing what an escape room is.
• Page for About - What is an escape room
• Page for Games - Showing each of the different games which can be played with links to booking page. We have one game to start - the surgeons shadows. A victorian doctors office and serial killers. Then a game coming soon which is aztec/mayan/jungle/harold Crane feel.
• FAQ Page
Nice to have
• Graphics for multiple players ie 2 players, 3 players, 4 players etc
• Dark and Mysterious feel.
• Inspiration from Puzzle Vault, Cipher Lodge, Quest Lockbox
Should not have
• Cartoony/childish. Pink.
• Not bloody or dripping letters etc - not cliche.
• Not horror themed.

```html
<!DOCTYPE html>
<html lang="en">
<head>
<meta charset="utf-8">
<title>About – What is an escape room?</title>
<link rel="stylesheet" href="https://fonts.googleapis.com/css2?family=Creepster&family=Playfair+Display:wght@900&family=Arimo:wght@400&display=swap">
<style>
  :root {
    --nav-red: #3f0002;
    --nav-rule: #6d6a70;
    --nav-text: #ffffff;
    --heading: #d2d0d1;
    --body-text: #ffffff;
    --scene-warm: #5b3d36;
    --scene-mid: #2a2436;
    --scene-cool: #12152b;
    --scene-top: #181a2b;
    --floor-warm: #9c4d42;
    --floor-cool: #5e3540;
    --floor-edge: #e8c49a;
  }
  * { margin: 0; padding: 0; box-sizing: border-box; }
  html, body { width: 1200px; height: 700px; overflow: hidden; background: var(--scene-top); }
  .page {
    position: relative;
    width: 1200px;
    height: 700px;
    overflow: hidden;
    font-family: "Arimo", Arial, sans-serif;
  }
  .dungeon-scene {
    position: absolute;
    inset: 0;
    background:
      linear-gradient(180deg, var(--scene-top) 0%, rgba(24,26,43,0) 40%),
      linear-gradient(100deg, var(--scene-warm) 0%, var(--scene-mid) 45%, var(--scene-cool) 100%);
  }
  .dungeon-floor {
    position: absolute;
    left: 0; right: 0; bottom: 0;
    height: 25px;
    background: linear-gradient(90deg, var(--floor-warm), var(--floor-cool));
    border-top: 2px solid var(--floor-edge);
  }
  .main-nav {
    position: absolute;
    top: 19px; left: 0;
    width: 1200px; height: 45px;
    background: var(--nav-red);
    border-bottom: 2px solid var(--nav-rule);
  }
  .main-nav a {
    position: absolute;
    top: 7px;
    transform: translateX(-50%);
    font-family: "Creepster", cursive;
    font-size: 30px;
    line-height: 32px;
    letter-spacing: 1px;
    color: var(--nav-text);
    text-decoration: none;
    white-space: nowrap;
  }
  .page-title {
    position: absolute;
    left: 126px; top: 132px;
    font-family: "Playfair Display", Georgia, serif;
    font-weight: 900;
    font-size: 82px;
    line-height: 90px;
    letter-spacing: -1px;
    color: var(--heading);
  }
  .section-title {
    position: absolute;
    left: 363px; top: 218px;
    font-family: "Playfair Display", Georgia, serif;
    font-weight: 900;
    font-size: 46px;
    line-height: 54px;
    color: var(--heading);
    white-space: nowrap;
  }
  .intro-panel {
    position: absolute;
    left: 120px; top: 274px;
    width: 1018px; height: 352px;
    background: linear-gradient(90deg, rgba(150,110,100,0.28), rgba(40,36,60,0.25) 50%, rgba(6,8,30,0.45));
  }
  .intro-text {
    position: absolute;
    left: 125px;
    font-size: 21px;
    line-height: 36px;
    letter-spacing: 0.4px;
    color: var(--body-text);
    white-space: nowrap;
  }
  .intro-text.first { top: 303px; }
  .intro-text.second { top: 483px; }
</style>
</head>
<body>
<div class="page">
  <div class="dungeon-scene" role="img" aria-label="Illustrated dungeon room with wooden beams, lit candles on a stool, a sword, a mace, a knight's helmet and shields">
    <div class="dungeon-floor"></div>
  </div>

  <nav class="main-nav">
    <a href="#" style="left:137px">HOME PAGE</a>
    <a href="#" style="left:332px">ABOUT</a>
    <a href="#" style="left:503px">GAMES</a>
    <a href="#" style="left:720px">CONTACT US</a>
    <a href="#" style="left:883px">FAQ</a>
    <a href="#" style="left:1048px">BOOK NOW</a>
  </nav>

  <h1 class="page-title">About</h1>
  <h2 class="section-title">What is an escape room ?</h2>

  <div class="intro-panel"></div>
  <p class="intro-text first">An escape room, also known as an escape game, is a game in which a team of players coopera-<br>tively discover clues, solve puzzles, and accomplish tasks in one or more rooms in order to prog-<br>ress and accomplish a specific goal in a limited amount of time. The goal is often to escape from<br>the site of the game.</p>
  <p class="intro-text second">Escape rooms became popular in North America, Europe and East Asia in the 2010s. Permanent<br>escape rooms in fixed locations were first opened in Asia and followed later in Hungary, Serbia,<br>Australia, New Zealand, Russia and South America</p>
</div>
</body>
</html>
```